High Resolution (300 dpi) Re-Creation of Poster

This project requires someone to try and replicate a poster that was done for a film. The designer never provided source files (Photo Shop) that we could edit or high resolution files that we could use for printing. We are not expecting a 100% perfect duplication; just try and get as close as you can and provide a few different variations that the producer can choose from. NOTE: I have full copyrights for this poster - I paid the designer through ArtHive and he deleted the file. I also have rights to the photo which comes from the film producer Karl Dunmore. The artist, Rolf Marchetti, was my uncle. I am working directly with the film producer including development of posters and distribution which you can verify at www.rolfmarchettilegacyfilm.com

Industry/Entity Type

Shop

Requirements
Must have
• Must include the image of the artist Rolf Marchetti per the image file provided and the sunset effect overall on the poster.
• Must be high resolution quality for printing which is 330 dpi
Nice to have
• Feel free to improve how the text shows up
• It would also be nice if the top of the head of the artist is not cut off at the top of the poster; i.e. move this down and color in some black hair so the complete head is included within the poster.
Should not have
• Do not get too creative - try and come as close to the original poster as possible

```html
<!DOCTYPE html>
<html lang="en">
<head>
<meta charset="utf-8">
<title>Rolf Marchetti — Night Cadence</title>
<link rel="stylesheet" href="https://fonts.googleapis.com/css2?family=Oranienbaum&family=Oswald:wght@400;500&family=Montserrat:wght@800&family=Archivo:wght@400&display=swap">
<style>
  :root {
    --page: #ffffff;
    --band: #0d0c0b;
    --gold: #e5b54a;
    --white: #ffffff;
    --ink: #141414;
    --sky-top: #c9ccd0;
    --sky-mid: #dfe1e2;
    --sun: #f6c53f;
    --portrait-light: #9b9b9b;
    --portrait-dark: #1c1c1c;
  }
  html, body { margin: 0; padding: 0; overflow: hidden; }
  body { width: 1200px; height: 1200px; background: var(--page); position: relative; }

  .poster {
    position: absolute; left: 198px; top: 0; width: 804px; height: 1200px;
    overflow: hidden; background: var(--band);
  }
  .sky {
    position: absolute; left: 0; top: 0; width: 804px; height: 860px;
    background: linear-gradient(180deg, var(--sky-top) 0%, var(--sky-mid) 35%, #d8d6cc 62%, #e9c878 78%, var(--sun) 87%, #b37a1c 100%);
  }
  .portrait { position: absolute; left: 0; top: 0; }
  .pianist {
    position: absolute; left: 522px; top: 732px; width: 232px; height: 128px;
    background: linear-gradient(180deg, rgba(20,16,10,0) 0%, rgba(20,16,10,.85) 40%, #14100a 100%);
  }

  .cast {
    position: absolute; left: 594px; top: 42px; width: 200px;
    text-align: center; margin: 0; padding: 0; list-style: none;
    font-family: "Oranienbaum", serif; color: var(--ink); font-size: 25px; line-height: 32.4px;
  }
  .cast-lead { font-family: "Oswald", sans-serif; color: var(--gold); font-weight: 500; font-size: 26px; line-height: 34px; }

  .credit { position: absolute; left: 45px; top: 682px; margin: 0; font-family: "Oswald", sans-serif; font-weight: 500; color: var(--gold); text-transform: uppercase; line-height: 1; }
  .credit-lead { font-size: 28px; padding-left: 53px; display: block; }
  .credit-name { font-size: 40px; display: block; margin-top: 6px; letter-spacing: .5px; }

  .titles { position: absolute; left: 0; top: 840px; }
  .titles text { fill: var(--white); }
  .title-name { font-family: "Montserrat", sans-serif; font-weight: 800; }
  .title-film { font-family: "Oswald", sans-serif; font-weight: 400; }
  .title-sub { font-family: "Oswald", sans-serif; font-weight: 500; }

  .site {
    position: absolute; left: 0; top: 1146px; width: 804px; margin: 0; text-align: center;
    font-family: "Archivo", sans-serif; font-size: 16px; letter-spacing: 7.6px; color: var(--white);
  }
</style>
</head>
<body>
<main class="poster">
  <div class="sky" role="img" aria-label="Cloudy sky fading into a golden sunset"></div>

  <svg class="portrait" width="804" height="860" viewBox="0 0 804 860" role="img" aria-label="Black and white portrait photograph of Rolf Marchetti in glasses, shown in profile">
    <defs>
      <linearGradient id="portraitTone" x1="0" y1="0" x2="0" y2="1">
        <stop offset="0" stop-color="var(--portrait-dark)"/>
        <stop offset=".2" stop-color="#6e6e6e"/>
        <stop offset=".55" stop-color="var(--portrait-light)"/>
        <stop offset="1" stop-color="var(--portrait-dark)"/>
      </linearGradient>
    </defs>
    <path d="M0 500 C20 420 40 200 90 110 C150 20 300 10 420 30 C500 45 540 90 555 160 C570 230 575 300 560 380 C555 430 520 470 495 500 C480 540 460 590 390 610 C370 650 380 720 410 860 L0 860 Z" fill="url(#portraitTone)"/>
  </svg>

  <div class="pianist" role="img" aria-label="Silhouette of a pianist at a grand piano against the sunset"></div>

  <ul class="cast">
    <li class="cast-lead">With...</li>
    <li>Glen Harlow</li>
    <li>Vince Caldera</li>
    <li>Nora Marchetti</li>
    <li>Lou Brantley</li>
    <li>Dale Whitcomb</li>
    <li>Arlo Penbrook</li>
    <li>Hank Lorimer</li>
    <li>Miles Fairbanks</li>
    <li>Roy Ashdown</li>
    <li>Ted Vollmering</li>
    <li>Sal Bertone</li>
    <li>Nick Castellano</li>
    <li>Owen Strand</li>
    <li>Curtis Hale</li>
    <li>Walt Drummond</li>
    <li>Leon Greenfield</li>
  </ul>

  <p class="credit">
    <span class="credit-lead">A film by</span>
    <span class="credit-name">Karl Dunmore</span>
  </p>

  <svg class="titles" width="804" height="260" viewBox="0 0 804 260">
    <text class="title-name" x="46" y="64" font-size="56" textLength="500" lengthAdjust="spacingAndGlyphs">ROLF MARCHETTI</text>
    <text class="title-film" x="46" y="190" font-size="112" textLength="712" lengthAdjust="spacingAndGlyphs">NIGHT CADENCE</text>
    <text class="title-sub" x="402" y="246" font-size="30" text-anchor="middle" textLength="540" lengthAdjust="spacingAndGlyphs">THE LIFE AND MUSIC OF ROLF MARCHETTI</text>
  </svg>

  <p class="site">WWW.ROLFMARCHETTILEGACYFILM.COM</p>
</main>
</body>
</html>
```